Copperfield Provisions Company Label

I need a label designed that will reflect the Copperfield Provisions Company. We produce and source locally meat products such as sausages, pates, terrines, mousses etc.... The label needs to communicate artistry, modernism, hand made, playfulness. We produce the finest meat products and utilize only locally sourced meat from the best farmers. All these things we hold in high regard and it needs to be reflected in the label. The label must also have a vintage feel since we are using vintage techniques of production. The first image file is my companies logo and should be used as a jumping off point.
Should be no larger then 4"x 4", I dont have specifics on shape i am open to anything. The packaging is ROP (reduced oxygen packaging) sometimes called cyo-vac packaging.
Please yield to the images i posted as inspiration in the direction i want. The logo does not have to be used, but i would like it in the same vein of design. Again artistry and graphics.
Target Market(s)
Consumer who care about the products they are consuming. These people frequent farmers markets and have a tend to buy locally even when it is more expensive.
Industry/Entity Type
It Company
Requirements
Must have
- Vintage imagery and a modern feel, a red and black color scheme. Other colors will be acceptable in the right taste. A statement of weight, use any for this case. Must have a place for the contents of the package, "Grass Fed Hot Dogs" for example.
Nice to have
- A old timely friendly butcher, a hand crank meat grinder, wooden butcher tables, cleavers.
Should not have
- Animal silhouettes

```html
<!DOCTYPE html>
<html lang="en">
<head>
<meta charset="utf-8">
<title>Copperfield Provisions Company – Grass Fed Hot Dogs Label</title>
<link rel="stylesheet" href="https://fonts.googleapis.com/css2?family=Francois+One&family=Pathway+Gothic+One&display=swap">
<style>
  :root {
    --page: #ffffff;
    --label-orange: #f15a22;
    --trim-gold: #f6c873;
    --panel-grey: #e9eaeb;
    --ink: #161616;
    --grass-green: #3f7e2a;
    --art-dark: #3a3a3a;
    --art-light: #c9cacc;
  }
  * { margin: 0; padding: 0; box-sizing: border-box; }
  html, body {
    width: 1200px;
    height: 1000px;
    overflow: hidden;
    background: var(--page);
  }
  .canvas {
    position: relative;
    width: 1200px;
    height: 1000px;
  }
  .label {
    position: absolute;
    left: 298px;
    top: 198px;
    width: 604px;
    height: 604px;
    background: var(--label-orange);
  }
  .label-panel {
    position: absolute;
    left: 24px;
    top: 24px;
    width: 556px;
    height: 556px;
    border-radius: 30px;
    border: 6px solid var(--trim-gold);
    background: var(--panel-grey);
    overflow: hidden;
  }
  .brand-name {
    position: absolute;
    left: 0;
    top: 20px;
    width: 100%;
    text-align: center;
    font-family: "Francois One", sans-serif;
    font-weight: 400;
    font-size: 100px;
    line-height: 1;
    color: var(--label-orange);
  }
  .brand-tagline {
    position: absolute;
    left: 0;
    top: 150px;
    width: 100%;
    text-align: center;
    font-family: "Pathway Gothic One", sans-serif;
    font-size: 56px;
    line-height: 70px;
    letter-spacing: 1px;
    color: var(--ink);
  }
  .product-name {
    position: absolute;
    left: 0;
    top: 246px;
    width: 100%;
    text-align: center;
    font-family: "Francois One", sans-serif;
    font-weight: 400;
    font-size: 44px;
    line-height: 1;
    letter-spacing: 1px;
    color: var(--grass-green);
  }
  .grinder-art {
    position: absolute;
    left: 60px;
    top: 292px;
    width: 334px;
    height: 250px;
    border-radius: 6px;
    background: linear-gradient(160deg, var(--art-light) 0%, #8d8e90 55%, var(--art-dark) 100%);
  }
  .net-weight {
    position: absolute;
    left: 395px;
    top: 479px;
    width: 140px;
    text-align: center;
    font-family: Arial, Helvetica, sans-serif;
    font-weight: 700;
    font-size: 16px;
    line-height: 26px;
    color: var(--ink);
  }
</style>
</head>
<body>
<main class="canvas">
  <section class="label">
    <div class="label-panel">
      <h1 class="brand-name">Copperfield</h1>
      <p class="brand-tagline">PROVISIONS COMPANY</p>
      <h2 class="product-name">GRASS FED HOT DOGS</h2>
      <div class="grinder-art" role="img" aria-label="Vintage engraving of a hand crank meat grinder clamped to a wooden butcher table, ground meat spilling onto a plate"></div>
      <p class="net-weight">Net Wt. 12 oz<br>(340g)</p>
    </div>
  </section>
</main>
</body>
</html>
```